Silver Kettle Studio Marketing Postcard

I need a 2 sided A6 postcard to distribute to potential clients. The postcard will include the business logo and information about the service we provide and contact information. I want it to be stylish and to compliment the business card. I've attached the business card and logo files as well as some text to use. I have other source files (.eps and.ai) if required please message me. I don't need the postal address or my position included on the postcard.
I am open to portrait or landscape designs, whatever you think is most stylish and eye catching.

```html
<!DOCTYPE html>
<html lang="en">
<head>
<meta charset="utf-8">
<title>Silver Kettle Studio – Postcard</title>
<link rel="stylesheet" href="https://fonts.googleapis.com/css2?family=Noto+Sans:ital,wght@0,400;0,700;1,400&display=swap">
<style>
  :root {
    --page: #ffffff;
    --navy: #0f1f33;
    --leaf-green: #76de10;
    --text: #ffffff;
  }
  html, body {
    margin: 0;
    padding: 0;
    width: 1200px;
    height: 1000px;
    overflow: hidden;
    background: var(--page);
  }
  .canvas {
    position: relative;
    width: 1200px;
    height: 1000px;
    font-family: "Noto Sans", Verdana, sans-serif;
    color: var(--text);
  }
  .postcard {
    position: absolute;
    left: 34px;
    top: 96px;
    width: 1136px;
    height: 806px;
    background: var(--navy);
    overflow: hidden;
  }
  .accent-band {
    position: absolute;
    inset: 0;
    width: 1136px;
    height: 806px;
  }
  .copy {
    position: absolute;
    left: 0;
    top: 0;
    width: 742px;
    text-align: center;
  }
  .copy p { margin: 0; }
  .headline {
    position: absolute;
    left: 0; right: 0;
    top: 28px;
    font-weight: 700;
    font-size: 25px;
    line-height: 33px;
    letter-spacing: 0.4px;
  }
  .intro {
    position: absolute;
    left: 0; right: 0;
    top: 142px;
    font-weight: 700;
    font-size: 25px;
    letter-spacing: 0.4px;
  }
  .body-text {
    position: absolute;
    left: 0; right: 0;
    font-size: 22px;
    line-height: 29px;
    letter-spacing: 0.3px;
  }
  .services-summary { top: 213px; }
  .advice-note { top: 333px; }
  .service-list {
    position: absolute;
    left: 158px;
    top: 417px;
    width: 440px;
    margin: 0;
    padding: 0;
    list-style: none;
    display: grid;
    grid-template-columns: 287px 1fr;
    row-gap: 6px;
    text-align: left;
    font-size: 22px;
    line-height: 29px;
    letter-spacing: 0.3px;
  }
  .service-list li {
    position: relative;
    padding-left: 19px;
  }
  .service-list li::before {
    content: "";
    position: absolute;
    left: 0;
    top: 6px;
    width: 7px;
    height: 17px;
    background: var(--leaf-green);
  }
  .tagline {
    position: absolute;
    left: 0; right: 0;
    top: 520px;
    font-weight: 700;
    font-size: 25px;
    letter-spacing: 0.4px;
  }
  .contact { top: 567px; }
  .contact em { font-style: italic; }
  .sign-off {
    position: absolute;
    left: 0; right: 0;
    top: 734px;
    font-weight: 700;
    font-size: 25px;
    letter-spacing: 0.4px;
  }
</style>
</head>
<body>
<main class="canvas">
  <section class="postcard">
    <svg class="accent-band" viewBox="0 0 1136 806" aria-hidden="true">
      <path d="M781 0 L1136 0 L1136 806 L966 806 C930 600 880 330 781 0 Z" fill="var(--leaf-green)"/>
    </svg>

    <div class="copy">
      <p class="headline">Do you feel frustrated by computers,<br>TVs, phones, tablets and countless<br>other digital devices?</p>
      <p class="intro">Silver Kettle Studio is here to help.</p>

      <p class="body-text services-summary">From a simple computer health check to the<br>purchase and installation of<br>home networks and digital services.</p>
      <p class="body-text advice-note">We also give useful product advice<br>and maintenance tips.</p>

      <ul class="service-list">
        <li>On site support</li>
        <li>Advice</li>
        <li>Installation</li>
        <li>Education</li>
      </ul>

      <p class="tagline">Let us help you tame your digital world.</p>

      <p class="body-text contact">Phone conversations are free<br><em>so call</em> Rowan on 0400 555 019,<br>email rowan@silverkettlestudio.com.au<br><em>or go to</em> www.silverkettlestudio.com.au<br><em>for more information.</em></p>

      <p class="sign-off">Problems Solved.</p>
    </div>
  </section>
</main>
</body>
</html>
```